Manuka Honey company needs a Upmarket, Luxury Website!

New Zealand, Taranaki based Manuka Honey company Marumaru Honey is looking for a new website, we are looking for an upmarket, luxury, serious website design. We export the highest quality quality Manuka Honey, straight from the Taranaki region.

Main export markets are Asia & Europe, also New Zealand & Australia.

Looking to have a beautiful, upmarket, serious, luxurious & graphical experience with mobile optimization in mind. Like the use of product staging/mockups

You can use copy from other websites to build the site and we will change the copy after the design is finished.

***Please include 'Honey Product' mockups in website.

*Will add illustrator files in coming days***

Feel free to make website functional in Shopify, Wordpress or WIX

Target Market(s)

Asia, Europe (main markets) New Zealand, Australia (Submarkets)

Coding

Coded - Design and coding required

Number of Pages Required

4 page

Requirements
Must have
• Home, Shop, About Us, Contact Us

Homepage to include:

Our Products
Company Video (video under construction)
What is MGO/UMF
Newsletter Opt-in

***(Not in Order)***

Please include 'Honey Product' mockups in website.
*Will add illustrator files in coming days
Nice to have
• FAQ & Partnership Inquiries (hyperlink in footer)

```html
<!DOCTYPE html>
<html lang="en">
<head>
<meta charset="utf-8">
<title>Marumaru Honey</title>
<link rel="stylesheet" href="https://fonts.googleapis.com/css2?family=Amatic+SC:wght@400;700&family=Raleway:wght@400;500;700;800&family=Nunito+Sans:wght@400;600&display=swap">
<style>
:root{
  --green:#8fbe00;
  --green-bright:#a6d21c;
  --purple:#7c3b86;
  --purple-dark:#6c2f78;
  --gold:#c9a54a;
  --ink:#1f1f1f;
  --text:#555555;
  --cream:#f8faef;
  --white:#ffffff;
  --dark:#222222;
}
*{margin:0;padding:0;box-sizing:border-box}
html,body{width:1200px;height:3600px;overflow:hidden}
body{position:relative;background:var(--white);font-family:"Nunito Sans",sans-serif;color:var(--text)}
.abs{position:absolute}
.display{font-family:"Amatic SC",cursive;font-weight:700;line-height:1}
.btn{position:absolute;display:flex;align-items:center;justify-content:center;font-family:"Raleway",sans-serif;font-weight:800;color:var(--white);background:var(--purple);text-decoration:none;letter-spacing:.3px}
.btn-pill{border-radius:30px;font-size:18px}
.copy{font-size:15.5px;line-height:25px;text-align:justify}

/* header */
.site-header{position:absolute;left:0;top:0;width:1200px;height:103px;background:var(--white);z-index:5}
.brand{position:absolute;left:102px;top:30px;display:flex;align-items:center;gap:14px}
.brand-dot{width:42px;height:42px;border-radius:50%;background:var(--gold)}
.brand-name{font-family:"Raleway",sans-serif;font-weight:500;font-size:25px;letter-spacing:4px;color:var(--gold)}
.main-nav a{position:absolute;top:47px;font-family:"Raleway",sans-serif;font-weight:500;font-size:14px;color:var(--ink);text-decoration:none}
.main-nav a.active{font-weight:700}
.header-icons svg{position:absolute;top:42px}
.cart-count{position:absolute;left:1104px;top:34px;width:20px;height:20px;border-radius:50%;background:var(--green);color:var(--white);font-size:11px;font-family:"Raleway",sans-serif;font-weight:700;display:flex;align-items:center;justify-content:center}

/* hero */
.hero-bg{position:absolute;left:0;top:103px;width:1200px;height:784px;background:linear-gradient(180deg,#eeeeed 0%,#e4e4e2 45%,#d8d6d0 70%,#cfcac1 100%)}
.hero-title{position:absolute;left:98px;top:288px;font-size:82px;color:var(--green);letter-spacing:2px;line-height:76px}
.hero-jars{position:absolute;left:542px;top:265px;width:556px;height:336px;border-radius:10px;background:linear-gradient(180deg,#1b1b1b 0%,#1b1b1b 18%,#a88a2e 22%,#c7a23b 60%,#8c7020 100%)}
.slider-dots span{position:absolute;left:1154px;width:12px;height:12px;border-radius:50%;background:#c4c4c4}
.slider-dots span.on{background:var(--green)}

/* about */
.about-photo{position:absolute;left:95px;top:821px;width:485px;height:430px;border-radius:50% 50% 46% 54% / 55% 60% 40% 45%;background:radial-gradient(circle at 40% 45%,#e0882a 0%,#e9b03c 45%,#f3cc5a 75%,#8a6a55 100%)}
.about-jar{position:absolute;left:380px;top:1050px;width:188px;height:250px;border-radius:10px;background:linear-gradient(180deg,#1b1b1b 0%,#1b1b1b 18%,#a88a2e 22%,#c7a23b 60%,#8c7020 100%)}
.section-title{font-size:62px;color:var(--ink);letter-spacing:2px}

/* shop */
.shop-bg{position:absolute;left:0;top:1320px;width:1200px;height:800px}
.card{position:absolute;background:var(--cream);box-shadow:0 0 6px rgba(0,0,0,.08)}
.card-featured{position:absolute;background:var(--green)}
.jar{position:absolute;border-radius:8px;background:linear-gradient(180deg,#1b1b1b 0%,#1b1b1b 20%,#a88a2e 25%,#c7a23b 60%,#8c7020 100%)}
.product-name{position:absolute;font-family:"Raleway",sans-serif;font-weight:800;font-size:17px;color:#3a3a3a;text-align:center;width:240px}
.product-price{position:absolute;font-family:"Raleway",sans-serif;font-weight:500;font-size:16px;color:#3a3a3a;text-align:center;width:240px}
.card-featured-name{font-size:19px;color:#4a5a10}
.card-featured-price{font-size:18px;color:#4a5a10}
.btn-square{font-size:15px}
.btn-outline{position:absolute;left:478px;top:1995px;width:246px;height:50px;border:2px solid var(--ink);background:var(--white);color:var(--ink);font-family:"Raleway",sans-serif;font-weight:800;font-size:15px;display:flex;align-items:center;justify-content:center}

/* video */
.video-photo{position:absolute;left:629px;top:2137px;width:483px;height:433px;border-radius:50% 50% 48% 52% / 60% 55% 45% 40%;background:radial-gradient(circle at 50% 55%,#8a5a22 0%,#c38b3c 40%,#dcd4c2 75%,#9db36a 100%)}
.play{position:absolute;left:816px;top:2322px}
.video-jar{position:absolute;left:580px;top:2347px;width:153px;height:202px}

/* family */
.family-photo{position:absolute;left:0;top:2540px;width:1200px;height:620px;background:linear-gradient(100deg,#ffffff 0%,#fbf3e2 25%,#e9a43a 45%,#d97e12 60%,#f2c24a 80%,#e6b86a 100%)}
.family-title{position:absolute;left:98px;top:2752px;font-size:58px;color:var(--ink);line-height:56px;letter-spacing:1px}
.family-copy{position:absolute;left:101px;top:2878px;width:400px;font-size:15.5px;line-height:25px;color:var(--text)}
.btn-family{position:absolute;left:98px;top:2973px;width:165px;height:45px;background:var(--green-bright);border:2px solid #2b3a00;color:#1f1f1f;font-family:"Raleway",sans-serif;font-weight:800;font-size:14px;display:flex;align-items:center;justify-content:center}

/* footer */
.footer-brand-dot{position:absolute;left:208px;top:3290px;width:50px;height:50px;border-radius:50%;background:var(--white)}
.footer-brand{position:absolute;left:110px;top:3365px;width:248px;text-align:center;font-family:"Raleway",sans-serif;font-weight:500;font-size:25px;letter-spacing:3px;color:var(--white)}
.footer-small{position:absolute;font-family:"Raleway",sans-serif;font-size:15px;color:var(--white)}
.footer-legal{font-size:13px}
.social span{position:absolute;top:3501px;width:24px;height:24px;border-radius:50%;background:var(--white)}
.footer-head{position:absolute;top:3294px;font-family:"Raleway",sans-serif;font-weight:800;font-size:16px;color:var(--white)}
.footer-links a{position:absolute;font-family:"Raleway",sans-serif;font-size:15px;color:var(--white);text-decoration:none}
.email-input{position:absolute;left:854px;top:3368px;width:258px;height:42px;background:var(--white);font-family:"Raleway",sans-serif;font-size:11px;color:#777;padding-left:22px;display:flex;align-items:center;letter-spacing:.5px}
.subscribe{position:absolute;left:856px;top:3421px;width:259px;height:42px;background:var(--dark);color:var(--white);font-family:"Raleway",sans-serif;font-weight:500;font-size:15px;display:flex;align-items:center;justify-content:center}
</style>
</head>
<body>

<header class="site-header">
  <div class="brand"><span class="brand-dot"></span><span class="brand-name">MARUMARU HONEY</span></div>
  <nav class="main-nav">
    <a class="active" style="left:458px">HOME</a>
    <a style="left:574px">SHOP</a>
    <a style="left:684px">ABOUT US</a>
    <a style="left:830px">CONTACT US</a>
  </nav>
  <div class="header-icons">
    <svg style="left:978px" width="22" height="22" viewBox="0 0 22 22" fill="none" stroke="#333" stroke-width="1.8"><circle cx="9" cy="9" r="7"/><path d="M14 14l6 6"/></svg>
    <svg style="left:1027px" width="22" height="22" viewBox="0 0 22 22" fill="none" stroke="#333" stroke-width="1.8"><circle cx="11" cy="7" r="5"/><path d="M2 21c0-5 4-8 9-8s9 3 9 8z"/></svg>
    <svg style="left:1075px" width="26" height="22" viewBox="0 0 26 22" fill="none" stroke="#333" stroke-width="1.8"><path d="M1 2h4l3 12h13l3-9H7"/><circle cx="10" cy="19" r="1.8"/><circle cx="19" cy="19" r="1.8"/></svg>
  </div>
  <div class="cart-count">0</div>
</header>

<section class="hero">
  <div class="hero-bg" role="img" aria-label="Misty sea and pale wooden tabletop backdrop"></div>
  <h1 class="hero-title display">WELCOME TO<br>TASTY MUNAKA<br>HONEY</h1>
  <a class="btn btn-pill" style="left:87px;top:534px;width:190px;height:51px">SHOP NOW</a>
  <div class="hero-jars" role="img" aria-label="Three jars of honey with black lids and black labels"></div>
  <div class="slider-dots"><span class="on" style="top:367px"></span><span style="top:393px"></span><span style="top:418px"></span></div>
  <svg class="abs" style="left:0;top:740px" width="1200" height="150" viewBox="0 0 1200 150"><path d="M0 90 C200 10 420 20 620 70 C820 120 1000 150 1200 147 L1200 150 L0 150 Z" fill="#ffffff"/></svg>
</section>

<section class="about">
  <div class="about-photo" role="img" aria-label="Honey dipper dripping honey into a glass pot among yellow flowers"></div>
  <div class="about-jar" role="img" aria-label="Honey jar with black lid and label"></div>
  <h2 class="section-title display abs" style="left:636px;top:920px">ABOUT US</h2>
  <p class="copy abs" style="left:636px;top:1005px;width:489px">Ilo inventore veritatis et quasi architecto beatae vitae dicta sunt explicabo. Nemo enim ipsam voluptatem quia voluptas sit aspernatur aut odit aut fugit, sed quia consequuntur magni dolores eos qui ratione voluptatem sequi nesciunt. Neque porro quisquam est, qui dolorem ipsum quia dolor</p>
  <a class="btn btn-pill" style="left:636px;top:1145px;width:191px;height:51px">SHOP NOW</a>
</section>

<section class="shop">
  <svg class="shop-bg" width="1200" height="800" viewBox="0 0 1200 800"><path d="M0 22 C200 70 380 80 600 40 C820 0 1000 0 1200 10 L1200 800 L0 800 Z" fill="#f8faef"/></svg>
  <h2 class="section-title display abs" style="left:0;width:1200px;text-align:center;top:1480px">SHOP NOW</h2>

  <div class="card" style="left:140px;top:1579px;width:905px;height:370px"></div>

  <div class="jar" role="img" aria-label="Honey jar product shot" style="left:224px;top:1613px;width:146px;height:189px"></div>
  <div class="product-name" style="left:174px;top:1822px">TASTY HONEY</div>
  <div class="product-price" style="left:174px;top:1848px">$60.99 USD</div>
  <a class="btn btn-square" style="left:221px;top:1886px;width:149px;height:39px">SHOP NOW</a>

  <div class="card-featured" style="left:409px;top:1560px;width:365px;height:411px"></div>
  <div class="jar" role="img" aria-label="Honey jar product shot" style="left:508px;top:1600px;width:168px;height:209px"></div>
  <div class="product-name card-featured-name" style="left:474px;top:1829px">TASTY HONEY</div>
  <div class="product-price card-featured-price" style="left:474px;top:1857px">$70.99 USD</div>
  <a class="btn btn-square" style="left:506px;top:1900px;width:176px;height:42px;font-size:16px">SHOP NOW</a>

  <div class="jar" role="img" aria-label="Honey jar product shot" style="left:817px;top:1613px;width:146px;height:189px"></div>
  <div class="product-name" style="left:777px;top:1822px">TASTY HONEY</div>
  <div class="product-price" style="left:777px;top:1848px">$90.99 USD</div>
  <a class="btn btn-square" style="left:824px;top:1886px;width:150px;height:39px">SHOP NOW</a>

  <a class="btn-outline">VIEW ALL PRODUCTS</a>
</section>

<section class="video">
  <h2 class="section-title display abs" style="left:109px;top:2248px">OUR VIDEO</h2>
  <p class="copy abs" style="left:109px;top:2335px;width:489px">Ilo inventore veritatis et quasi architecto beatae vitae dicta sunt explicabo. Nemo enim ipsam voluptatem quia voluptas sit aspernatur aut odit aut fugit, sed quia consequuntur magni dolores eos qui ratione voluptatem sequi nesciunt. Neque porro quisquam est, qui dolorem ipsum quia dolor sit</p>
  <a class="btn btn-pill" style="left:109px;top:2474px;width:191px;height:51px">SHOP NOW</a>
  <div class="video-photo" role="img" aria-label="Beekeeper holding a honeycomb frame covered with bees"></div>
  <svg class="play" width="92" height="92" viewBox="0 0 92 92" fill="none" stroke="#ffffff" stroke-width="6"><circle cx="46" cy="46" r="42"/><path d="M36 28 L64 46 L36 64 Z" stroke-linejoin="round"/></svg>
  <div class="jar video-jar" role="img" aria-label="Honey jar with black lid and label"></div>
</section>

<section class="family">
  <div class="family-photo" role="img" aria-label="Wooden honey dipper dripping golden honey into a jar"></div>
  <svg class="abs" style="left:0;top:2530px" width="1200" height="120" viewBox="0 0 1200 120"><path d="M0 0 L1200 0 L1200 12 C900 110 400 130 0 85 Z" fill="#ffffff"/></svg>
  <h2 class="family-title display">BEST PRODUCT<br>FOR YOUR FAMILY</h2>
  <p class="family-copy">Curabitur vel dolor ultrices ipsum dictum tristique Praesent vitae lacus Ut velit enim vestibulum non Aermentum nec hendrerit quis leo</p>
  <a class="btn-family">SHOP NOW</a>
</section>

<footer class="site-footer">
  <svg class="abs" style="left:0;top:3040px" width="1200" height="560" viewBox="0 0 1200 560"><path d="M0 33 C350 170 800 150 1200 18 L1200 560 L0 560 Z" fill="#7c3b86"/><path d="M110 60 C450 140 800 135 1130 38" fill="none" stroke="#8fbe00" stroke-width="6" stroke-linecap="round"/></svg>

  <span class="footer-brand-dot"></span>
  <div class="footer-brand">MARUMARU HONEY</div>
  <div class="footer-small" style="left:108px;top:3438px">Copyright © 2020 manuka honey</div>
  <div class="footer-small footer-legal" style="left:110px;top:3469px">Privacy &nbsp;| &nbsp;Terms of Use</div>
  <div class="social" role="img" aria-label="Social media links">
    <span style="left:110px"></span><span style="left:149px"></span><span style="left:188px"></span><span style="left:227px"></span>
  </div>

  <div class="footer-head" style="left:438px">NAVIGATE</div>
  <nav class="footer-links">
    <a style="left:440px;top:3333px">Home</a>
    <a style="left:440px;top:3366px">About Us</a>
    <a style="left:440px;top:3399px">Products</a>
    <a style="left:440px;top:3432px">Shop Now</a>
    <a style="left:440px;top:3465px">Cotnact Us</a>
  </nav>

  <div class="footer-head" style="left:632px">RESOURCES</div>
  <nav class="footer-links">
    <a style="left:634px;top:3333px">Privacy Policy</a>
    <a style="left:634px;top:3366px">Terms</a>
    <a style="left:634px;top:3399px">My Account</a>
    <a style="left:634px;top:3432px">Shipping &amp; Return</a>
    <a style="left:634px;top:3465px">Cart</a>
  </nav>

  <div class="footer-head" style="left:853px">CONNECT WITH US</div>
  <div class="footer-small" style="left:856px;top:3333px">Sign up here to stay up to date</div>
  <div class="email-input">EMAIL ADDRESS</div>
  <div class="subscribe">SUBSCRIBE</div>
</footer>

</body>
</html>
```